Graphics Design of Physics Book

Hi
Size : 8" x 11.25"
We are education book Publication Company and would like to have book cover for "Physics" it has 4 volumes. All 4 having the same color scheme and design except the volume no.
Blue is my personal favorite but u can use any color. Want to have a band at the bottom of the cover to place our Logo “VORLIN Education” a PDF of the same is attached, or you can place logo anywhere according to ur design.
I need “Physics” as title of the book to be visible prominently.
And volume and volume no. should also be Visible and eye catching I prefer a Graphic to enhance the Volume No.
A background pattern can also be a option (it should be vector form so that color can be change later)
Please do not offer any cut and paste design I need very professional presentation.
Volume and Number can be in metallic 3D (CMYK) effect.
only Professional presentation will get feedback.
I have provided a sample artwork for reference do not follow it but can be a reference what I needed !

Target Market(s)

Students Class 9th to 12th

Industry/Entity Type

Education

Font styles to use
Serif

Colors
3176b5
0555a3
85abd2
cadf82
abd036
9bcb3c

Requirements
Must have
• Eye catching.
• “Physics” as title of the book to be visible prominently.
• volume and volume no. should also be Visible and eye catching
• I prefer a Graphic to enhance the Volume No.
• Icons for
• 1. Questions and answers
• 2. Theory Notes
• 3. Tips & Tricks
• 4. Previous Year's Reference Questions
• 5. Covers Complete Syllabus
Nice to have
• decent seamless background or metallic 3d effect (not to be print in special Ink) design should only be in CMYK.
Should not have
• Physics related Pictures or Icons (Specially E=mc2) or any scientist photograph or I Need pure graphic design

```html
<!DOCTYPE html>
<html lang="en">
<head>
<meta charset="utf-8">
<title>Physics Cover</title>
<link href="https://fonts.googleapis.com/css2?family=Tinos:wght@400;700&family=Oswald:wght@400;500&family=Montserrat:wght@700&display=swap" rel="stylesheet">
<style>
  :root {
    --navy: #1c1a6b;
    --deep: #0f0f4a;
    --line-blue: #3f8fe0;
    --icon-blue: #2f8be0;
    --icon-ring: #8cc4f2;
    --white: #ffffff;
    --gold-light: #f3ecc0;
    --gold-dark: #8a7a3a;
    --badge-bg: #121212;
    --ink: #111111;
  }
  html, body {
    margin: 0;
    padding: 0;
    width: 919px;
    height: 1200px;
    overflow: hidden;
    background: var(--white);
  }
  .cover {
    position: relative;
    width: 919px;
    height: 1200px;
    overflow: hidden;
    background: var(--navy);
  }
  .pattern {
    position: absolute;
    inset: 0;
    background:
      radial-gradient(ellipse at 45% 40%, rgba(15,15,74,0.9) 0%, rgba(15,15,74,0) 55%),
      linear-gradient(90deg, #25308a 0%, #1d2070 30%, #2a52b0 52%, #1c2a80 68%, #2b5cc0 85%, #22348e 100%);
  }
  .volume-badge {
    position: absolute;
    left: 74px;
    top: 60px;
    width: 108px;
    height: 130px;
    background: var(--badge-bg);
    border: 2px solid var(--gold-dark);
    border-radius: 12px;
    box-sizing: border-box;
    text-align: center;
  }
  .volume-number {
    display: block;
    margin-top: 6px;
    font-family: "Tinos", serif;
    font-weight: 700;
    font-size: 86px;
    line-height: 86px;
    letter-spacing: -4px;
    color: var(--gold-light);
    text-shadow: 2px 3px 0 var(--gold-dark);
  }
  .volume-label {
    display: block;
    font-family: "Tinos", serif;
    font-weight: 700;
    font-size: 17px;
    color: var(--white);
    margin-top: 4px;
  }
  .publisher {
    position: absolute;
    left: 620px;
    top: 72px;
    width: 158px;
    height: 54px;
    background: var(--white);
    text-align: center;
    font-family: "Montserrat", sans-serif;
    font-weight: 700;
    color: var(--ink);
    font-size: 18px;
    line-height: 54px;
    letter-spacing: 0.5px;
  }
  .title {
    position: absolute;
    left: 0;
    right: 0;
    top: 470px;
    margin: 0;
    text-align: center;
    font-family: "Tinos", serif;
    font-weight: 400;
    font-size: 190px;
    line-height: 1;
    color: var(--white);
    transform: scaleY(1.3);
    transform-origin: center top;
    letter-spacing: -2px;
  }
  .features {
    position: absolute;
    left: 70px;
    top: 990px;
    width: 800px;
    height: 170px;
    display: flex;
  }
  .feature {
    flex: 1;
    text-align: center;
    border-left: 1px solid rgba(255,255,255,0.8);
    padding-top: 28px;
  }
  .feature:first-child { border-left: none; }
  .feature svg { display: block; margin: 0 auto; }
  .feature-label {
    margin-top: 8px;
    font-family: "Oswald", sans-serif;
    font-size: 12px;
    line-height: 15px;
    color: var(--white);
    text-shadow: 1px 1px 0 rgba(0,0,0,0.5);
  }
</style>
</head>
<body>
  <div class="cover">
    <div class="pattern" role="img" aria-label="Background pattern of fine interlacing light-blue curved lines on deep navy"></div>

    <div class="volume-badge">
      <span class="volume-number">VI</span>
      <span class="volume-label">VOLUMES</span>
    </div>

    <div class="publisher">VORLIN Education</div>

    <h1 class="title">PHYSICS</h1>

    <div class="features">
      <div class="feature">
        <svg width="70" height="70" viewBox="0 0 70 70" aria-hidden="true">
          <circle cx="35" cy="35" r="33" fill="var(--icon-blue)" stroke="var(--icon-ring)" stroke-width="3"/>
          <text x="35" y="44" text-anchor="middle" font-family="Tinos, serif" font-style="italic" font-size="26" fill="#fff">Q&amp;A</text>
        </svg>
        <div class="feature-label">Questions &amp; Answers</div>
      </div>
      <div class="feature">
        <svg width="70" height="70" viewBox="0 0 70 70" aria-hidden="true">
          <circle cx="35" cy="35" r="33" fill="var(--icon-blue)" stroke="var(--icon-ring)" stroke-width="3"/>
          <rect x="20" y="18" width="22" height="30" fill="#fff" stroke="#1a4f8f" stroke-width="1.5"/>
          <rect x="27" y="22" width="22" height="30" fill="#fff" stroke="#1a4f8f" stroke-width="1.5"/>
          <path d="M31 29h14M31 34h14M31 39h14M31 44h14" stroke="#1a4f8f" stroke-width="1.5"/>
        </svg>
        <div class="feature-label">Theory Notes</div>
      </div>
      <div class="feature">
        <svg width="70" height="70" viewBox="0 0 70 70" aria-hidden="true">
          <circle cx="35" cy="35" r="33" fill="var(--icon-blue)" stroke="var(--icon-ring)" stroke-width="3"/>
          <path d="M22 36l9 9 17-19" fill="none" stroke="#fff" stroke-width="5" stroke-linecap="round" stroke-linejoin="round"/>
        </svg>
        <div class="feature-label">Tips &amp; Tricks</div>
      </div>
      <div class="feature">
        <svg width="70" height="70" viewBox="0 0 70 70" aria-hidden="true">
          <circle cx="35" cy="35" r="33" fill="var(--icon-blue)" stroke="var(--icon-ring)" stroke-width="3"/>
          <rect x="23" y="17" width="24" height="34" fill="#fff" stroke="#1a4f8f" stroke-width="1.5"/>
          <path d="M27 24h16M27 29h16M27 34h16M27 39h16M27 44h10" stroke="#1a4f8f" stroke-width="1.5"/>
        </svg>
        <div class="feature-label">Previous Year’s<br>Reference Questions</div>
      </div>
      <div class="feature">
        <svg width="70" height="70" viewBox="0 0 70 70" aria-hidden="true">
          <circle cx="35" cy="35" r="33" fill="var(--icon-blue)" stroke="var(--icon-ring)" stroke-width="3"/>
          <rect x="18" y="40" width="34" height="9" rx="2" fill="#fff" stroke="#1a4f8f" stroke-width="1.5"/>
          <rect x="21" y="31" width="30" height="9" rx="2" fill="#fff" stroke="#1a4f8f" stroke-width="1.5"/>
          <rect x="19" y="22" width="30" height="9" rx="2" fill="#fff" stroke="#1a4f8f" stroke-width="1.5"/>
        </svg>
        <div class="feature-label">Covers Complete<br>Syllabus</div>
      </div>
    </div>
  </div>
</body>
</html>
```